Business cards for Harbourline Supply Pty Ltd that import building products into Australia from China
Target Market(s)
Business to Business
Industry/Entity Type
Business
Contact Information for Business Card
Front: Logo and Business Name
Rear:
Vernon Ashcombe
General Manager
Mobile: 0427 619 354
email: vern@harbourlinesupply.com.au
alternative email: vern@coastwardgoods.com.au
web: www.harbourlinesupply.com.au
Adelaide, Brisbane and Darwin
Colors
ec1f27
fbee3d

```html
<!DOCTYPE html>
<html lang="en">
<head>
<meta charset="utf-8">
<title>Harbourline Supply – Business Cards</title>
<link href="https://fonts.googleapis.com/css2?family=Montserrat:wght@400;500;600&display=swap" rel="stylesheet">
<style>
  :root {
    --backdrop: #e4e5e7;
    --card: #151515;
    --brand-red: #ec1f27;
    --brand-grey: #b4b4b4;
    --text-light: #c9c9c9;
    --rule: #6c6c6c;
  }
  html, body {
    margin: 0;
    padding: 0;
    width: 1200px;
    height: 1000px;
    overflow: hidden;
    background: var(--backdrop);
    font-family: "Montserrat", sans-serif;
  }
  .canvas {
    position: relative;
    width: 1200px;
    height: 1000px;
  }
  .card {
    position: absolute;
    width: 520px;
    height: 296px;
    background: var(--card);
    box-shadow: 0 4px 10px rgba(0,0,0,0.25);
  }
  .card--details { left: 180px; top: 160px; }
  .card--front { left: 415px; top: 503px; }

  .wordmark {
    display: flex;
    align-items: center;
    gap: 10px;
    color: var(--brand-grey);
    font-weight: 600;
    white-space: nowrap;
  }
  .wordmark__dot {
    background: var(--brand-red);
    border-radius: 50%;
    flex: none;
  }
  .card--details .wordmark {
    position: absolute;
    right: 34px;
    top: 44px;
    font-size: 23px;
  }
  .card--details .wordmark__dot { width: 12px; height: 12px; }
  .card--front .wordmark {
    position: absolute;
    left: 50%;
    top: 50%;
    transform: translate(-50%, -50%);
    font-size: 36px;
    gap: 14px;
  }
  .card--front .wordmark__dot { width: 18px; height: 18px; }

  .person {
    position: absolute;
    left: 34px;
    top: 146px;
  }
  .person__name {
    margin: 0;
    color: var(--brand-red);
    font-size: 16px;
    font-weight: 500;
    letter-spacing: 0.3px;
    text-transform: uppercase;
  }
  .person__role {
    margin: 2px 0 0;
    color: var(--text-light);
    font-size: 14px;
    font-weight: 400;
  }
  .card__rule {
    position: absolute;
    left: 34px;
    right: 34px;
    top: 196px;
    height: 1px;
    background: var(--rule);
  }
  .contact {
    position: absolute;
    top: 210px;
    margin: 0;
    padding: 0;
    list-style: none;
    color: var(--text-light);
    font-size: 12.5px;
    line-height: 18px;
  }
  .contact--left { left: 34px; }
  .contact--right { left: 262px; }
  .contact__item {
    display: flex;
    align-items: flex-start;
    gap: 9px;
    margin-bottom: 2px;
  }
  .contact__icon {
    width: 12px;
    height: 12px;
    margin-top: 3px;
    flex: none;
    fill: var(--brand-red);
  }
</style>
</head>
<body>
<main class="canvas">

  <section class="card card--details" aria-label="Business card, contact side">
    <div class="wordmark"><span class="wordmark__dot"></span>Harbourline Supply</div>

    <div class="person">
      <p class="person__name">Vernon Ashcombe</p>
      <p class="person__role">General Manager</p>
    </div>

    <div class="card__rule"></div>

    <ul class="contact contact--left">
      <li class="contact__item">
        <svg class="contact__icon" viewBox="0 0 12 12" aria-hidden="true"><path d="M3 0h6a1 1 0 0 1 1 1v10a1 1 0 0 1-1 1H3a1 1 0 0 1-1-1V1a1 1 0 0 1 1-1zm.4 1.2v8.6h5.2V1.2z"/></svg>
        <span>0427 619 354</span>
      </li>
      <li class="contact__item">
        <svg class="contact__icon" viewBox="0 0 12 12" aria-hidden="true"><path d="M6 0a4.5 4.5 0 0 1 4.5 4.5C10.5 8 6 12 6 12S1.5 8 1.5 4.5A4.5 4.5 0 0 1 6 0zm0 2.6a1.9 1.9 0 1 0 0 3.8 1.9 1.9 0 0 0 0-3.8z"/></svg>
        <span>27 Quayside Road<br>Darwin, NT 0810</span>
      </li>
    </ul>

    <ul class="contact contact--right">
      <li class="contact__item">
        <svg class="contact__icon" viewBox="0 0 12 12" aria-hidden="true"><path d="M0 2.5h12v7H0zm0 .4L6 6.6l6-3.7V2.5H0z"/></svg>
        <span>vern@harbourlinesupply.com.au</span>
      </li>
      <li class="contact__item">
        <svg class="contact__icon" viewBox="0 0 12 12" aria-hidden="true"><path d="M0 2.5h12v7H0zm0 .4L6 6.6l6-3.7V2.5H0z"/></svg>
        <span>vern@coastwardgoods.com.au</span>
      </li>
      <li class="contact__item">
        <svg class="contact__icon" viewBox="0 0 12 12" aria-hidden="true"><path d="M6 0a6 6 0 1 0 0 12A6 6 0 0 0 6 0zm0 1.2c.8.8 1.4 2.3 1.5 4.2h-3C4.6 3.5 5.2 2 6 1.2zM3.3 5.4H1.2a4.8 4.8 0 0 1 3.1-3.9 8 8 0 0 0-1 3.9zm0 1.2a8 8 0 0 0 1 3.9 4.8 4.8 0 0 1-3.1-3.9zm1.2 0h3c-.1 1.9-.7 3.4-1.5 4.2-.8-.8-1.4-2.3-1.5-4.2zm4.2 0h2.1a4.8 4.8 0 0 1-3.1 3.9 8 8 0 0 0 1-3.9zm0-1.2a8 8 0 0 0-1-3.9 4.8 4.8 0 0 1 3.1 3.9z"/></svg>
        <span>www.harbourlinesupply.com.au</span>
      </li>
    </ul>
  </section>

  <section class="card card--front" aria-label="Business card, brand side">
    <div class="wordmark"><span class="wordmark__dot"></span>Harbourline Supply</div>
  </section>

</main>
</body>
</html>
```